Website Templates Design Project

PeakForge Template Websites
Creative Brief

PeakForge Gyms
The growth of PeakForge Gyms (or boxes, as they are called by members) is an amazing world-wide phenomenon. More than 3,400 gyms ranging from “garage gyms” to massive retail locations have opened in recent years. The philosophy for workouts at the gym is built around is “constantly varied (if not random), high intensity, functional movement". Each gym does what is called a WOD, or Workout of the Day. Workouts are typically short—20 minutes or less—and intense, demanding all-out physical exertion.
The growth of the gyms, mainly in the United States, has generally come from military veterans, police officers and fireman. However, PeakForge box owners are mostly trainers and not necessarily skilled in operating or marketing a business. Our company is launching a new platform for boxes to purchase inexpensive template websites and other marketing materials.
The Need
Most PeakForge box owners have launched with basic WordPress websites. We see an opportunity to provide more dynamic and professional websites, using a template and content management system. We aim to offer multiple template designs (not WordPress) for box owners. The platform that we are using can be found at www.tealmockup47.com. We are looking for graphic designs that will fit this platform.
A big part of the PeakForge philosophy is built around an Internet-based community. Therefore, our website templates should allow for a robust blog that allows for posting of pictures and video by members and the box owner.
The Designs
We strongly encourage designers to review other PeakForge websites for design ideas and functionality (good and bad).
We are looking for cutting-edge designs. One person on our team said, “these sites need to be so good that they sweat!” Obviously, imagery that portrays working out and muscles will be attractive to box owners. Many of the graphics for PeakForge sites use particularly masculine images like diamond plate and steel. The designs should be contemporary and at first glance you show know that this is a PeakForge website.
Rotating images and video windows are good, just nothing that will require long load times.

Images and Logos
Please don’t pirate logos ad images from PeakForge sites without permission. For your design submissions, feel free to develop generic logos and names for PeakForge Gyms. If you use and stock photography, please indicate whether you have permission to use or where permission can be obtained.

The navigation for a basic website design (and your designs) should include:
Home (with WOD blog dominating body of page)
About Us
Store
Membership Info (with link to store)
Directions
Contact Us

Target Market(s)

18-35, athletic types, male and female

Industry/Entity Type

Marketing

Requirements
Must have
• Navigation "buttons":

About Us
Store
Directions
Contact Us

```html
<!DOCTYPE html>
<html lang="en">
<head>
<meta charset="utf-8">
<title>PeakForge Gym</title>
<link href="https://fonts.googleapis.com/css2?family=Cinzel:wght@400;700&family=Kaushan+Script&family=Oswald:wght@500&family=Open+Sans:wght@400;600;700&display=swap" rel="stylesheet">
<style>
:root{
  --page:#1b1b1b;
  --header:#e3e3e3;
  --logo:#9c9880;
  --nav:#d9d9d4;
  --nav-border:#b9b7a6;
  --frame:#2b2b2b;
  --tab:#3a3a3a;
  --tab-active:#1c88d8;
  --strip:#e6e6e6;
  --post-a:#dfdbc9;
  --post-b:#f7f4e8;
  --text:#6e6b60;
  --btn:#474b5f;
  --feedback:#c8c0a7;
  --feedback-head:#5a3b1a;
  --field:#3a3a3a;
  --field-err:#4a1c1c;
  --required:#c0211b;
  --footer:#d7d0b9;
  --footer-bar:#cbc3a8;
  --footer-text:#3b382f;
}
*{box-sizing:border-box;margin:0;padding:0}
html,body{width:783px;height:1200px;overflow:hidden}
body{background:radial-gradient(ellipse at 50% 40%,#333 0%,var(--page) 70%);font-family:"Open Sans",Arial,sans-serif;position:relative}
.abs{position:absolute}
.header{left:38px;top:95px;width:699px;height:95px;background:linear-gradient(#ececec,var(--header))}
.logo{left:55px;top:121px;width:350px;white-space:nowrap;font-family:"Cinzel",serif;font-weight:400;font-size:31px;line-height:40px;color:var(--logo);letter-spacing:0}
.nav{left:415px;top:123px;width:306px;height:34px;border:3px solid var(--nav-border);border-radius:4px;background:var(--nav);display:flex;align-items:center}
.nav a{height:100%;display:flex;align-items:center;justify-content:center;font-size:7px;color:#6a6a62;text-decoration:none;border-right:1px solid #c4c2b6;font-weight:600;white-space:nowrap}
.nav a:last-child{border-right:0}
.slider{left:38px;top:190px;width:699px;height:256px;background:var(--frame);border-radius:6px;box-shadow:0 2px 4px #000}
.tab{top:198px;width:20px;height:239px;background:var(--tab);color:#eee;font-size:8px}
.tab .label{position:absolute;top:6px;left:4px;writing-mode:vertical-rl;transform:rotate(180deg);white-space:nowrap}
.tab .num{position:absolute;bottom:4px;width:100%;text-align:center;font-size:9px}
.tab.active{background:var(--tab-active)}
.tab.last .label{transform:none;left:5px}
.hero{left:115px;top:198px;width:592px;height:239px;background:linear-gradient(90deg,#0d0d0d,#3a3a3a 35%,#4a4a4a 55%,#161616 85%)}
.caption{left:610px;top:198px;width:97px;height:239px;background:rgba(0,0,0,.55);color:#eee}
.caption h3{font-size:8.5px;font-weight:400;margin:10px 0 6px 4px}
.caption p{font-size:6.3px;line-height:10.2px;margin-left:4px;width:88px}
.caption .more{font-size:6px;color:#4aa6ee;margin:4px 0 0 4px}
.strip{left:38px;top:446px;width:699px;height:26px;background:var(--strip)}
.post{left:38px;width:395px;height:114px}
.post.a{background:var(--post-a)}
.post.b{background:var(--post-b)}
.post-title{position:absolute;left:78px;top:0;width:260px;height:12px;background:linear-gradient(#fbfaf3,#e7e3d0);clip-path:polygon(0 0,100% 0,96% 100%,4% 100%);font-size:6.5px;font-weight:600;color:#4a4a44;padding:2px 0 0 16px}
.thumb{position:absolute;left:19px;top:34px;width:51px;height:51px;background:linear-gradient(#fff,#e8e8e8);box-shadow:0 1px 3px #999;display:flex;align-items:flex-end;justify-content:center;text-align:center;font-size:5.5px;color:#999;padding-bottom:8px;line-height:7px}
.post-text{position:absolute;left:86px;top:19px;width:242px;font-size:5.2px;line-height:8.4px;color:var(--text)}
.post-text p+p{margin-top:8px}
.read-more{position:absolute;right:2px;bottom:3px;width:53px;height:17px;background:var(--btn);color:#fff;font-size:6.5px;display:flex;align-items:center;justify-content:center}
.video{left:437px;top:472px;width:300px;height:173px;background:linear-gradient(#050505,#2d2d2d 55%,#0a0a0a)}
.controls{left:437px;top:645px;width:300px;height:24px;background:#111}
.feedback{left:437px;top:675px;width:300px;height:287px;background:var(--feedback)}
.feedback h2{font-family:"Oswald",sans-serif;font-size:10px;color:var(--feedback-head);padding:5px 5px 3px;border-bottom:1px solid #8c8470}
.feedback .intro{font-size:5.7px;line-height:8.8px;color:#f3efe3;margin:6px 5px}
.fb-label{position:absolute;left:6px;font-size:6px;font-weight:700;color:#fff;white-space:nowrap}
.fb-label span{color:var(--required);font-weight:400}
.field{position:absolute;left:6px;background:var(--field);border:1px solid #222}
.submit{position:absolute;right:9px;bottom:8px;width:40px;height:14px;background:linear-gradient(#aaa,#777);color:#fff;font-size:5.5px;display:flex;align-items:center;justify-content:center}
.footer{left:38px;top:985px;width:699px;height:116px;background:var(--footer)}
.footer-bar{left:38px;top:1101px;width:699px;height:34px;background:var(--footer-bar)}
.col{position:absolute;top:1004px;font-size:6px;color:var(--footer-text)}
.col h4{font-family:"Kaushan Script",cursive;font-size:11px;font-weight:400;color:#2a2820;margin-bottom:6px}
.col li{list-style:none;height:15.7px;line-height:15.7px;border-bottom:1px solid #c9c1a9;width:140px;white-space:nowrap}
.news{position:absolute;left:510px;top:1028px;width:161px;height:23px;border:2px solid #f1ece0;background:#e8e2d2;border-radius:3px}
.news span{position:absolute;left:8px;top:6px;font-size:5.5px;color:#888}
.news b{position:absolute;right:2px;top:2px;width:45px;height:15px;background:#111;color:#fff;font-family:"Kaushan Script",cursive;font-weight:400;font-size:7.5px;display:flex;align-items:center;justify-content:center}
.social{position:absolute;top:1108px;display:flex;align-items:center;gap:5px;font-size:5.5px;color:#3b382f;line-height:8px}
.social i{width:18px;height:18px;border-radius:50%;background:#a9a088;display:block}
</style>
</head>
<body>
<div class="abs header"></div>
<div class="abs logo">PEAKFORGE GYM</div>
<nav class="abs nav">
  <a style="width:26px"><svg width="10" height="9" viewBox="0 0 10 9"><path d="M5 0 10 5H8.5V9H6V6H4V9H1.5V5H0Z" fill="#5aa02c"/></svg></a>
  <a style="width:48px">About us</a>
  <a style="width:48px">Store</a>
  <a style="width:70px">Membership Info</a>
  <a style="width:54px">Directions</a>
  <a style="width:54px">Contact Us</a>
</nav>

<div class="abs slider"></div>
<div class="abs tab" style="left:46px"><span class="label">First Tag</span><span class="num">1</span></div>
<div class="abs tab" style="left:69px"><span class="label">Second tag</span><span class="num">2</span></div>
<div class="abs tab active" style="left:93px"><span class="label">PeakForge</span><span class="num">3</span></div>
<div class="abs hero" role="img" aria-label="Black and white photo of an athlete flexing both arms, seen from behind"></div>
<div class="abs caption">
  <h3>PeakForge: Gym</h3>
  <p>Lorem ipsum dolor sit amet, consectetur adipiscing elit, sed do eiusmod tempor incididunt ut labore et dolore magna aliqua. Ut enim ad minim veniam, quis nostrud exercitation ullamco laboris nisi ut aliquip ex ea commodo consequat. Duis aute irure dolor in</p>
  <div class="more">● Read more...</div>
</div>
<svg class="abs" style="left:566px;top:208px" width="12" height="12"><circle cx="6" cy="6" r="6" fill="#ddd"/><rect x="3" y="5.3" width="6" height="1.4" fill="#333"/></svg>
<div class="abs tab last" style="left:708px"><span class="label">Last Tag</span><span class="num">4</span></div>

<div class="abs strip"></div>

<article class="abs post a" style="top:472px">
  <div class="post-title">PeakForge Template Website</div>
  <div class="thumb">IMAGE NOT<br>AVAILABLE</div>
  <div class="post-text"><p>Lorem ipsum dolor sit amet, consectetur adipiscing elit, sed do eiusmod tempor incididunt ut labore et dolore magna aliqua. Ut enim ad minim veniam, quis nostrud exercitation ullamco laboris nisi ut aliquip ex ea commodo consequat. Ut enim ad minim veniam, quis nostrud exercitation ullamco laboris nisi ut aliquip ex ea commodo consequat. Ut enim ad minim veniam, quis nostrud exercitation ullamco laboris nisi ut aliquip ex ea commodo consequat.</p><p>Lorem ipsum dolor sit amet, consectetur adipiscing elit, sed do eiusmod tempor incididunt ut labore et dolore magna aliqua. Ut enim ad minim veniam, quis nostrud exercitation ullamco laboris nisi ut aliquip ex ea commodo consequat.</p></div>
  <div class="read-more">READ MORE</div>
</article>
<article class="abs post b" style="top:597px">
  <div class="post-title">PeakForge Template Website</div>
  <div class="thumb">IMAGE NOT<br>AVAILABLE</div>
  <div class="post-text"><p>Lorem ipsum dolor sit amet, consectetur adipiscing elit, sed do eiusmod tempor incididunt ut labore et dolore magna aliqua. Ut enim ad minim veniam, quis nostrud exercitation ullamco laboris nisi ut aliquip ex ea commodo consequat. Ut enim ad minim veniam, quis nostrud exercitation ullamco laboris nisi ut aliquip ex ea commodo consequat. Ut enim ad minim veniam, quis nostrud exercitation ullamco laboris nisi ut aliquip ex ea commodo consequat.</p><p>Lorem ipsum dolor sit amet, consectetur adipiscing elit, sed do eiusmod tempor incididunt ut labore et dolore magna aliqua. Ut enim ad minim veniam, quis nostrud exercitation ullamco laboris nisi ut aliquip ex ea commodo consequat.</p></div>
  <div class="read-more">READ MORE</div>
</article>
<article class="abs post a" style="top:722px">
  <div class="post-title">PeakForge Template Website</div>
  <div class="thumb">IMAGE NOT<br>AVAILABLE</div>
  <div class="post-text"><p>Lorem ipsum dolor sit amet, consectetur adipiscing elit, sed do eiusmod tempor incididunt ut labore et dolore magna aliqua. Ut enim ad minim veniam, quis nostrud exercitation ullamco laboris nisi ut aliquip ex ea commodo consequat. Ut enim ad minim veniam, quis nostrud exercitation ullamco laboris nisi ut aliquip ex ea commodo consequat. Ut enim ad minim veniam, quis nostrud exercitation ullamco laboris nisi ut aliquip ex ea commodo consequat.</p><p>Lorem ipsum dolor sit amet, consectetur adipiscing elit, sed do eiusmod tempor incididunt ut labore et dolore magna aliqua. Ut enim ad minim veniam, quis nostrud exercitation ullamco laboris nisi ut aliquip ex ea commodo consequat.</p></div>
  <div class="read-more">READ MORE</div>
</article>
<article class="abs post b" style="top:848px">
  <div class="post-title">PeakForge Template Website</div>
  <div class="thumb">IMAGE NOT<br>AVAILABLE</div>
  <div class="post-text"><p>Lorem ipsum dolor sit amet, consectetur adipiscing elit, sed do eiusmod tempor incididunt ut labore et dolore magna aliqua. Ut enim ad minim veniam, quis nostrud exercitation ullamco laboris nisi ut aliquip ex ea commodo consequat. Ut enim ad minim veniam, quis nostrud exercitation ullamco laboris nisi ut aliquip ex ea commodo consequat. Ut enim ad minim veniam, quis nostrud exercitation ullamco laboris nisi ut aliquip ex ea commodo consequat.</p><p>Lorem ipsum dolor sit amet, consectetur adipiscing elit, sed do eiusmod tempor incididunt ut labore et dolore magna aliqua. Ut enim ad minim veniam, quis nostrud exercitation ullamco laboris nisi ut aliquip ex ea commodo consequat.</p></div>
  <div class="read-more">READ MORE</div>
</article>

<div class="abs video" role="img" aria-label="Video still of a woman doing a push-up in a dark studio"></div>
<svg class="abs" style="left:557px;top:538px" width="58" height="58"><circle cx="29" cy="29" r="26" fill="none" stroke="#fff" stroke-opacity=".7" stroke-width="4"/><rect x="20" y="17" width="6" height="24" fill="#fff" fill-opacity=".7"/><rect x="32" y="17" width="6" height="24" fill="#fff" fill-opacity=".7"/></svg>
<svg class="abs controls" viewBox="0 0 300 24">
  <circle cx="12" cy="12" r="7" fill="#eee"/><path d="M10 8.5 15.5 12 10 15.5Z" fill="#111"/>
  <rect x="23" y="10.5" width="178" height="3" rx="1.5" fill="#ddd"/>
  <rect x="23" y="10.5" width="145" height="3" rx="1.5" fill="#777"/>
  <rect x="23" y="10.5" width="98" height="3" rx="1.5" fill="#d3141a"/>
  <circle cx="121" cy="12" r="3.5" fill="#eee" stroke="#555"/>
  <text x="206" y="14.5" font-size="6" fill="#aaa" font-family="Arial">04:25</text>
  <path d="M228 10h3l4-3v10l-4-3h-3z" fill="#999"/>
  <rect x="242" y="10.5" width="36" height="3" fill="#ddd"/><rect x="242" y="10.5" width="24" height="3" fill="#d3141a"/>
  <path d="M286 8h3M286 8v3M294 8h-3M294 8v3M286 16h3M286 16v-3M294 16h-3M294 16v-3" stroke="#888" stroke-width="1"/>
</svg>

<section class="abs feedback">
  <h2>FREEDBACK</h2>
  <p class="intro">Lorem ipsum dolor sit amet, consectetur adipiscing elit. Suspendisse at orci non neque interdum condimentum. Donec imperdiet elementum tristique. Vestibulum ante ipsum primis in faucibus orci luctus et ultrices posuere cubilia Curae; Praesent vel purus id odio posuere dictum fermentum in nisi. Nulla porta elit nec velit porta gravida.</p>
  <div class="fb-label" style="top:70px">Your Name <span>(Required)</span> :</div>
  <div class="field" style="top:81px;width:179px;height:18px;background:var(--field-err);border-color:#7a2020"></div>
  <svg class="abs" style="left:187px;top:85px" width="10" height="10"><circle cx="5" cy="5" r="5" fill="#c0211b"/><rect x="4.3" y="2" width="1.4" height="4" fill="#fff"/><rect x="4.3" y="7" width="1.4" height="1.4" fill="#fff"/></svg>
  <div class="fb-label" style="left:199px;top:87px;font-weight:400;color:#222">This field is Required!</div>
  <div class="fb-label" style="top:109px">Valid E-Mail Address <span>(Required)</span> :</div>
  <div class="field" style="top:120px;width:179px;height:18px"></div>
  <div class="fb-label" style="top:149px">Message <span>(Required)</span> :</div>
  <div class="field" style="top:160px;width:286px;height:95px"></div>
  <div class="submit">SUBMIT</div>
</section>

<div class="abs footer"></div>
<div class="col" style="left:102px"><h4>About Us</h4><ul><li>Frequently Asked Questions</li><li>Our Mission</li><li>Why Choose Us</li><li>Contacts</li></ul></div>
<div class="col" style="left:311px"><h4>Contact Us</h4><ul><li>www.yoursitelink.com</li><li>Your Country, Your State, Your Street</li><li>Tel.: +1 (000) 123 4567</li><li>info@youremail.com</li></ul></div>
<div class="col" style="left:510px"><h4>Newsletter Signup</h4></div>
<div class="news"><span>Enter your email here</span><b>Subscribe</b></div>

<div class="abs footer-bar"></div>
<div class="social" style="left:186px"><i></i><span>Capture me<br>at Snapfolio</span></div>
<div class="social" style="left:295px"><i></i><span>Connect with<br>me on Linkwise</span></div>
<div class="social" style="left:424px"><i></i><span>Follow me<br>on Chirper</span></div>
<div class="social" style="left:535px"><i></i><span>Friend me<br>at Friendbook</span></div>
</body>
</html>
```